Social Media Graphics - Harbor Climb REVISED

Create 6-7 individual social media graphics (square size) to encourage folks to join our online course called:

The Lantern Ledger Plan
How to Launch a Multi-Million Business From Scratch
Sign Up Today!

IMPORTANT: Make the largest and most prominent text on the graphic be: How to Launch a Multi-Million Business From Scratch

For the color scheme of the graphics, let's try a blue color palette; make sure the graphics appeal to both men and women

Make sure each graphic contains 1 of the 3 pics attached (crop pic as needed); and make sure one of the graphics is all TEXT only.

Target Market(s)

men and women looking to start a business

Industry/Entity Type

Entrepreneurship

Colors
0054AA
0677BA
7BADD7
CADEEF
E8F1F8

Requirements
Must have
• All the text and use the 3 pics provided; one graphic can be all text; Simple, modern design that's easy to read

```html
<!DOCTYPE html>
<html lang="en">
<head>
<meta charset="utf-8">
<title>The Lantern Ledger Plan – Sign Up Today</title>
<link href="https://fonts.googleapis.com/css2?family=Anton&family=Oswald:wght@600;700&display=swap" rel="stylesheet">
<style>
  :root {
    --bg-deep: #0c1a9c;
    --bg-mid: #2f42c2;
    --bg-light: #3d62e0;
    --panel-navy: #07003a;
    --label-ink: #1e1f3a;
    --white: #ffffff;
  }
  html, body {
    margin: 0;
    padding: 0;
    width: 1200px;
    height: 1200px;
    overflow: hidden;
  }
  .graphic {
    position: relative;
    width: 1200px;
    height: 1200px;
    overflow: hidden;
  }
  .graphic__backdrop {
    position: absolute;
    inset: 0;
    background:
      radial-gradient(ellipse 70% 50% at 20% 15%, var(--bg-light) 0%, transparent 70%),
      radial-gradient(ellipse 60% 45% at 45% 100%, var(--bg-light) 0%, transparent 70%),
      linear-gradient(160deg, var(--bg-mid) 0%, var(--bg-mid) 45%, var(--bg-deep) 100%);
  }
  .graphic__art {
    position: absolute;
    inset: 0;
  }
  .course-label {
    fill: var(--white);
  }
  .course-label__text {
    font-family: "Oswald", sans-serif;
    font-weight: 700;
    font-size: 98px;
    fill: var(--label-ink);
  }
  .headline-panel {
    fill: var(--panel-navy);
  }
  .headline {
    font-family: "Anton", sans-serif;
    fill: var(--white);
  }
  .headline__line--large { font-size: 184px; }
  .headline__line--small { font-size: 130px; }
  .cta__rule {
    stroke: var(--white);
    stroke-width: 2;
  }
  .cta__text {
    font-family: "Oswald", sans-serif;
    font-weight: 700;
    font-size: 52px;
    fill: var(--white);
  }
</style>
</head>
<body>
  <main class="graphic">
    <div class="graphic__backdrop" role="img" aria-label="Abstract blue background with sweeping curved light streaks"></div>

    <svg class="graphic__art" width="1200" height="1200" viewBox="0 0 1200 1200" xmlns="http://www.w3.org/2000/svg">
      <g class="course-label-group">
        <rect class="course-label" x="103" y="180" width="994" height="111" rx="9"/>
        <text class="course-label__text" x="600" y="268" text-anchor="middle" textLength="919" lengthAdjust="spacingAndGlyphs">THE LANTERN LEDGER PLAN</text>
      </g>

      <g class="headline-group">
        <rect class="headline-panel" x="41" y="377" width="1119" height="633" rx="26"/>
        <text class="headline headline__line--large" x="600" y="598" text-anchor="middle" textLength="916" lengthAdjust="spacingAndGlyphs">HOW TO LAUNCH</text>
        <text class="headline headline__line--large" x="600" y="781" text-anchor="middle" textLength="916" lengthAdjust="spacingAndGlyphs">A MULTI-MILLION</text>
        <text class="headline headline__line--small" x="600" y="950" text-anchor="middle" textLength="922" lengthAdjust="spacingAndGlyphs">BUSINESS FROM SCRATCH</text>
      </g>

      <g class="cta">
        <line class="cta__rule" x1="41" y1="1095" x2="432" y2="1095"/>
        <line class="cta__rule" x1="762" y1="1095" x2="1160" y2="1095"/>
        <text class="cta__text" x="600" y="1112" text-anchor="middle" textLength="309" lengthAdjust="spacingAndGlyphs">SIGN UP TODAY</text>
      </g>
    </svg>
  </main>
</body>
</html>
```